Christmas Banner for frontpage of website

New online scarf store just opened needs a Christmas Banner stating Free Delivery (UK only). Also if it could incorporate guaranteed Christmas delivery if ordered before 18th (might be too wordy though?) I would really like it to bring some colour to the page. The page is currently black and white with a pink accent and is very simple which is why I would like something modern and elegant, simple but with some colour. It is a shopify store I understand the banner size should be 950px by 290px the website is www.velmorrow.co.uk

Target Market(s)

Ladies

Industry/Entity Type

Store

Requirements
Should not have
• Not to look tacky.

```html
<!DOCTYPE html>
<html lang="en">
<head>
<meta charset="utf-8">
<title>Christmas Free Delivery Banner</title>
<link rel="stylesheet" href="https://fonts.googleapis.com/css2?family=Quicksand:wght@400;500&display=swap">
<style>
  :root {
    --paper: #ffffff;
    --berry: #b8241d;
    --berry-glow: rgba(196, 48, 40, 0.55);
    --spruce: #1d7c71;
    --spruce-glow: rgba(29, 124, 113, 0.55);
    --mint: #7fcbc2;
    --mint-glow: rgba(127, 203, 194, 0.75);
    --mint-soft: #cfeae6;
  }
  html, body {
    margin: 0;
    padding: 0;
    width: 1200px;
    height: 366px;
    overflow: hidden;
    background: var(--paper);
  }
  .banner {
    position: relative;
    width: 1200px;
    height: 366px;
    overflow: hidden;
    background: var(--paper);
    font-family: "Quicksand", "Trebuchet MS", sans-serif;
  }
  .banner__festive-pattern {
    position: absolute;
    inset: 0;
    background:
      radial-gradient(ellipse 430px 120px at 600px 292px, var(--paper) 70%, rgba(255,255,255,0) 100%),
      radial-gradient(circle 110px at 700px 110px, var(--berry-glow), rgba(196,48,40,0) 100%),
      radial-gradient(circle 90px at 470px 70px, var(--berry-glow), rgba(196,48,40,0) 100%),
      radial-gradient(circle 80px at 1130px 200px, var(--berry-glow), rgba(196,48,40,0) 100%),
      radial-gradient(circle 70px at 330px 160px, var(--berry-glow), rgba(196,48,40,0) 100%),
      radial-gradient(circle 120px at 430px 150px, var(--spruce-glow), rgba(29,124,113,0) 100%),
      radial-gradient(circle 110px at 1000px 230px, var(--spruce-glow), rgba(29,124,113,0) 100%),
      radial-gradient(circle 100px at 790px 40px, var(--spruce-glow), rgba(29,124,113,0) 100%),
      radial-gradient(circle 150px at 60px 120px, var(--mint-glow), rgba(127,203,194,0) 100%),
      radial-gradient(circle 140px at 250px 60px, var(--mint-glow), rgba(127,203,194,0) 100%),
      radial-gradient(circle 150px at 980px 70px, var(--mint-glow), rgba(127,203,194,0) 100%),
      radial-gradient(circle 150px at 1160px 320px, var(--mint-glow), rgba(127,203,194,0) 100%),
      radial-gradient(circle 110px at 60px 300px, var(--mint-glow), rgba(127,203,194,0) 100%),
      linear-gradient(180deg, var(--mint-soft) 0%, var(--paper) 100%);
  }
  .banner__message {
    position: absolute;
    left: 0;
    right: 0;
    top: 224px;
    text-align: center;
  }
  .banner__headline {
    margin: 0;
    color: var(--berry);
    font-weight: 500;
    font-size: 47px;
    line-height: 1;
  }
  .banner__headline-note {
    font-size: 16px;
    font-weight: 400;
  }
  .banner__subline {
    margin: 6px 0 0;
    color: var(--spruce);
    font-weight: 500;
    font-size: 37px;
    line-height: 1;
  }
</style>
</head>
<body>
  <div class="banner">
    <div class="banner__festive-pattern" role="img" aria-label="Scattered Christmas motifs in teal and red: snowflakes, candy canes, baubles, gift boxes, bows, stockings, trees and gingerbread figures"></div>
    <div class="banner__message">
      <h1 class="banner__headline">Free Delivery<span class="banner__headline-note">(UK only)</span></h1>
      <p class="banner__subline">Guaranteed Christmas delivery if ordered before 18th.</p>
    </div>
  </div>
</body>
</html>
```